Car Dealership Poster

Need a poster created to promote our Referrral Program - portrait layout 3'x5'. Below is our Referral Progam website page for referance. See attchaed file for out logo.

https://brantleyautohausnj.example/get-paid-for-referrals/

Colors
00AB8E
00BBA5
67D7C9
C6EFE9
E9F9F6

```html
<!DOCTYPE html>
<html lang="en">
<head>
<meta charset="utf-8">
<title>Refer &amp; Earn – Brantley Autohaus</title>
<link rel="stylesheet" href="https://fonts.googleapis.com/css2?family=Montserrat:ital,wght@0,500;0,600;0,700;0,800;1,800;1,900&display=swap">
<style>
  :root {
    --panel-green: #0d7a45;
    --panel-green-light: #1aa866;
    --accent-green: #16a86a;
    --ghost-green: #19c777;
    --band-green: #0f9a63;
    --street-dark: #2a2a2a;
    --street-mid: #4a4a4a;
    --ink-black: #050505;
    --white: #ffffff;
  }
  * { margin: 0; padding: 0; box-sizing: border-box; }
  html, body { width: 720px; height: 1200px; overflow: hidden; background: var(--ink-black); }
  .poster {
    position: relative;
    width: 720px;
    height: 1200px;
    overflow: hidden;
    font-family: "Montserrat", sans-serif;
    color: var(--white);
    background: var(--ink-black);
  }
  .street-photo {
    position: absolute;
    left: 0; top: 0;
    width: 720px; height: 930px;
    background: linear-gradient(180deg, #1e1e1e 0%, var(--street-mid) 45%, #3a3a3a 75%, var(--ink-black) 100%);
  }
  .promo-panel {
    position: absolute;
    left: 94px; top: 0;
    width: 531px; height: 790px;
    background: linear-gradient(180deg, var(--panel-green) 0%, var(--panel-green-light) 55%, rgba(26,168,102,0.55) 85%, rgba(26,168,102,0) 100%);
  }
  .brand-name {
    position: absolute;
    left: 0; top: 36px;
    width: 720px;
    text-align: center;
    font-weight: 800;
    line-height: 1;
    letter-spacing: 1px;
  }
  .brand-name .line-main { display: block; font-size: 40px; }
  .brand-name .line-sub { display: block; font-size: 24px; letter-spacing: 5px; margin-top: 6px; }
  .intro {
    position: absolute;
    left: 0; top: 145px;
    width: 720px;
    text-align: center;
    font-size: 15.5px;
    font-weight: 500;
    line-height: 22px;
  }
  .headline {
    position: absolute;
    left: 0; top: 204px;
    width: 720px;
    text-align: center;
    font-weight: 900;
    font-style: italic;
    font-size: 108px;
    line-height: 90px;
    letter-spacing: -2px;
  }
  .ghost-tagline {
    position: absolute;
    top: 486px;
    font-weight: 900;
    font-style: italic;
    font-size: 56px;
    line-height: 56px;
    color: var(--ghost-green);
    opacity: 0.7;
    letter-spacing: -1px;
  }
  .ghost-tagline span { display: block; }
  .ghost-tagline .t-with { margin-left: 340px; }
  .ghost-tagline .t-brand { margin-left: 178px; }
  .ghost-tagline .t-sub { margin-left: 262px; opacity: 0.65; }
  .vehicle-photo {
    position: absolute;
    left: 72px; top: 645px;
    width: 576px; height: 280px;
    border-radius: 90px 120px 30px 30px;
    background: radial-gradient(ellipse at 45% 45%, #3ccf6a 0%, #22a850 45%, #0f6b30 80%, #0a0a0a 100%);
  }
  .details {
    position: absolute;
    left: 0; top: 944px;
    width: 720px;
    text-align: center;
    font-size: 15.5px;
    font-weight: 500;
    line-height: 22px;
  }
  .phone-band {
    position: absolute;
    left: 0; top: 1031px;
    width: 720px; height: 55px;
    background: var(--band-green);
    display: flex; align-items: center; justify-content: center;
    font-size: 27px;
    font-weight: 700;
    letter-spacing: 5px;
  }
  .address {
    position: absolute;
    left: 0; top: 1107px;
    width: 720px;
    text-align: center;
    font-size: 15px;
    font-weight: 700;
  }
  .website {
    position: absolute;
    left: 0; top: 1150px;
    width: 720px;
    text-align: center;
    font-size: 15px;
    font-weight: 700;
    letter-spacing: 3.5px;
  }
</style>
</head>
<body>
<main class="poster">
  <div class="street-photo" role="img" aria-label="Black and white photo of a city street lined with tall buildings"></div>
  <div class="promo-panel"></div>

  <header class="brand-name">
    <span class="line-main">BRANTLEY</span>
    <span class="line-sub">AUTOHAUS</span>
  </header>

  <p class="intro">Brantley Autohaus rewards you for spreading the word<br>about our amazing deals and top-notch vehicles.</p>

  <h1 class="headline">REFER<br>&amp;<br>EARN</h1>

  <div class="ghost-tagline" aria-hidden="true">
    <span class="t-with">WITH</span>
    <span class="t-brand">BRANTLEY</span>
    <span class="t-sub">AUTOHAUS</span>
  </div>

  <div class="vehicle-photo" role="img" aria-label="Photo of a green luxury SUV with black wheels"></div>

  <p class="details">Earn a $250 referral credit everytime a referral of yours buys a vehicle from us.<br>Referral must be a new customer to Brantley Autohaus.<br>Ask about our Referral Program and start earning rewards today!</p>

  <div class="phone-band">+1 609-555-0182</div>

  <p class="address">Address: 214 Harbor Ave, Millbrook, NJ 08099, United States</p>
  <p class="website">BRANTLEYAUTOHAUSNJ.EXAMPLE</p>
</main>
</body>
</html>
```